Secret agents need a new website

We organize child birthdays with a special agents in london & Bristol.

Current design does not grab people attention, and they leave website too soon.

Colors. Up to 3 main colors, but maybe black + green + white, or blact + red + white, would suit our secret operations website.

Current website:
www.moonjumble.co.uk

Dear designers, thanks very much for working on our design.

Please try to make like a SPECIAL YOUNG AGENT TRAINING WEBSITE, all other
entertainers have childish websites, and we want to differentiate from them.

Not sure if it helps, but I like this design very much:

Guys,

I am looking for spy/secret agent/action themed design. You submitting awesome designs, and if I have another business, I just choose any of them at it would be perfect. But I want spy/secret agent/action themed.

Please feel free to add elements like:

1. Yellow, or RED line CRIME SCENE DO NOT CROSS
2. Some words or phrases can be black background - white text. 
3. Some stamps like this:
http://www.plenvoria.com/pic-48120957/stock-vector-assorted-office-ink-marks-classified-private-etc.html?src=qTm4Lo-bRwNxZ3e-p81KcE-1-16

4.spy guys http://www.plenvoria.com/pic-39418275/stock-vector-sleuth-in-long-overcoat-vintage-clip-art.html?src=hdWpRmTeQoXs4v9bnaLjCf-1-9

Do not make too much elements, I like simple designs, less details.  

PLEASE NO CHILDS WITH GUNS, and better NO GUNS at all. 

Target Market(s)

Audience: Woman, but should look cool for kids too.
(Please DO NOT make design childish)

Requirements
Must have
• Please take a look at current website
• 1. Texts should be easy to read and not too small.
• 2. White/bright background
• 3. Lead form should stay on page
• 4. Header, and footer should be not too big.
• 5. Infographic is not needed
• Extra elements
• 1. Company blog
• 2. Client zone
• 3. Venue finder
• 4. How to pay deposit
Nice to have
• We accept
• Quidlo
• marrowfeld
• (please browse logos)
• On header would be better to use
• MoonJumble.co.uk
• But also add somethere, in association with Fen-rally.co.uk.
• Please use logo with .co.uk
• In archive you will find without background if needed too.

```html
<!DOCTYPE html>
<html lang="en">
<head>
<meta charset="utf-8">
<title>Fen-rally.co.uk – Spy Birthday Party</title>
<link href="https://fonts.googleapis.com/css2?family=Fjalla+One&family=Courier+Prime&family=Open+Sans:wght@400;600;700&display=swap" rel="stylesheet">
<style>
  :root {
    --ink: #2b2522;
    --hero-bg: #3b302b;
    --cream: #e9e5d3;
    --gold: #c9962a;
    --bronze: #8a6d3b;
    --question: #7a4b14;
    --body-text: #333;
    --muted: #777;
    --green: #8dc63f;
    --white: #fff;
  }
  * { box-sizing: border-box; margin: 0; padding: 0; }
  html, body { width: 671px; height: 1200px; overflow: hidden; background: var(--white); }
  body { position: relative; font-family: 'Open Sans', sans-serif; color: var(--body-text); }
  .abs { position: absolute; }

  .brand { left: 30px; top: 40px; display: flex; align-items: center; gap: 8px;
    font-family: 'Fjalla One', sans-serif; font-size: 26px; color: var(--ink); }
  .brand-mark { width: 18px; height: 18px; background: var(--green); }

  .btn { background: var(--cream); border-radius: 6px; font-family: 'Fjalla One', sans-serif;
    display: flex; align-items: center; justify-content: center; color: var(--ink); text-decoration: none; }
  .btn-top { left: 502px; top: 24px; width: 134px; height: 35px; font-size: 21px; }
  .call-label { right: 35px; top: 68px; font-size: 9px; color: var(--gold); }
  .call-phone { right: 35px; top: 78px; font-family: 'Fjalla One', sans-serif; font-size: 14px; color: var(--gold); }

  .main-nav { right: 35px; top: 113px; display: flex; gap: 23px; }
  .main-nav a { font-family: 'Fjalla One', sans-serif; font-size: 19px; color: var(--ink); text-decoration: none; }

  .hero { left: 26px; top: 140px; width: 615px; height: 311px; background: var(--hero-bg); border-radius: 6px; }
  .hero-agent { left: 34px; top: 104px; width: 222px; height: 347px;
    background: linear-gradient(180deg, #2e6b4e 0%, #4a4a45 45%, #5b5a55 100%); border-radius: 4px; }
  .hero-stamp { left: 232px; top: 182px; width: 236px; height: 58px; background: linear-gradient(90deg,#6e9b2a,#8dc63f);
    transform: rotate(-8deg); opacity: .85; }
  .hero-kit { left: 440px; top: 140px; width: 186px; height: 96px;
    background: linear-gradient(135deg,#e9b94f 0%,#c9a465 45%,#d8ccb2 100%); }
  .hero-copy { left: 249px; top: 272px; width: 380px; font-family: 'Courier Prime', monospace;
    font-size: 19.5px; line-height: 25px; letter-spacing: 1px; color: var(--white); }
  .deposit-paper { left: 384px; top: 368px; width: 236px; height: 62px; background: #b59b6a; transform: rotate(3deg); border-radius: 3px; }
  .btn-deposit { left: 378px; top: 373px; width: 233px; height: 51px; font-size: 25px; color: var(--bronze); }

  .intro { left: 35px; width: 605px; font-size: 10.4px; line-height: 12px; }
  .intro-1 { top: 462px; }
  .intro-2 { top: 500px; }

  .photo { background: linear-gradient(160deg,#b58a5e,#7a5a3e); }
  .photo-1 { left: 35px; top: 536px; width: 91px; height: 136px; }
  .photo-2 { left: 128px; top: 536px; width: 102px; height: 136px; background: linear-gradient(160deg,#b4a090,#8e7fb0); }
  .photo-3 { left: 35px; top: 676px; width: 91px; height: 136px; background: linear-gradient(160deg,#8b6a4e,#c23a2e); }
  .photo-4 { left: 128px; top: 676px; width: 102px; height: 136px; background: linear-gradient(160deg,#7b5a3e,#d8552e); }

  .party-copy { left: 240px; top: 532px; width: 395px; font-size: 10.4px; line-height: 11.5px; }
  .id-card { left: 240px; top: 612px; width: 394px; height: 200px;
    background: linear-gradient(90deg,#111 0%,#111 42%,#e8e8e8 42%,#f4f4f4 100%); }

  .faq-title { left: 42px; top: 836px; font-family: 'Fjalla One', sans-serif; font-size: 23px; color: var(--ink); }
  .faq { width: 275px; }
  .faq h3 { font-size: 10.2px; font-weight: 700; color: var(--question); margin-bottom: 3px; }
  .faq p { font-size: 7.8px; line-height: 9.6px; color: var(--body-text); }
  .faq p + p { margin-top: 9px; }
  .faq-l { left: 42px; }
  .faq-r { left: 352px; }
  .row-1 { top: 874px; }
  .row-2 { top: 938px; }
  .row-3 { top: 1003px; }

  .cta-bar { left: 26px; top: 1110px; width: 615px; height: 58px; background: var(--hero-bg); border-radius: 6px; }
  .cta-agent { left: 48px; top: 1072px; width: 60px; height: 96px; background: linear-gradient(180deg,#6b5e52,#1e1a18); border-radius: 4px; }
  .btn-cta { left: 170px; top: 1122px; width: 135px; height: 36px; font-size: 21px; color: var(--bronze); }
  .cta-label { left: 329px; top: 1134px; font-size: 10.5px; color: var(--white); }
  .cta-phone { left: 424px; top: 1127px; font-family: 'Fjalla One', sans-serif; font-size: 18px; color: var(--green); }

  .footer-links { left: 0; width: 671px; top: 1172px; text-align: center; font-size: 8.5px; color: var(--ink); }
  .footer-links a { color: var(--ink); text-decoration: none; }
  .copyright { left: 0; width: 671px; top: 1183px; text-align: center; font-size: 7.5px; color: var(--muted); }
</style>
</head>
<body>
  <header>
    <div class="abs brand"><span class="brand-mark"></span>Fen-rally.co.uk</div>
    <a class="abs btn btn-top" href="#">INQUIRE NOW</a>
    <div class="abs call-label">or call us at</div>
    <div class="abs call-phone">020 3947 5018</div>
    <nav class="abs main-nav">
      <a href="#">HOME</a><a href="#">EQUIPMENT</a><a href="#">INVITATIONS</a><a href="#">PARTY BAGS</a><a href="#">PRICES</a>
    </nav>
  </header>

  <section>
    <div class="abs hero"></div>
    <div class="abs hero-stamp" role="img" aria-label="Green 'Top Secret' rubber stamp"></div>
    <div class="abs hero-kit" role="img" aria-label="Envelope, compass and field manual"></div>
    <div class="abs hero-agent" role="img" aria-label="Young agent in a hat and suit looking through a magnifying glass"></div>
    <p class="abs hero-copy">Capture your kids imagination with a Spy Birthday party in London, Bristol</p>
    <div class="abs deposit-paper"></div>
    <a class="abs btn btn-deposit" href="#">HOW TO DEPOSIT?</a>
  </section>

  <main>
    <p class="abs intro intro-1">Every parent wants to give their child the best birthday party, but we don't always have the time to plan and prepare for an extra special birthday party with the wow factor.</p>
    <p class="abs intro intro-2">We created this Spy party to be fun from beginning to end. Your child will send their guests colour top secret invitations to a party where they will take part in Secret Agent Training. The children will be so excited that they won't be able to stop talking about it.</p>

    <div class="abs photo photo-1" role="img" aria-label="Boy exploring spy gear"></div>
    <div class="abs photo photo-2" role="img" aria-label="Girl wearing spy sunglasses"></div>
    <div class="abs photo photo-3" role="img" aria-label="Boy working on a spy gadget"></div>
    <div class="abs photo photo-4" role="img" aria-label="Boy taking part in a spy game"></div>

    <p class="abs party-copy">At the party all the children will become special agents, trying out spy gear and finding out how to be a good spy in our fun secret agent games. It's a great way to get the children interested in new things, working together in teams and using their imagination. Every child that takes part will receive a 'Spy School Secret Agent' certificate and a Spy Party Bag to take away and continue the fun with their friends at home and at school.</p>
    <div class="abs id-card" role="img" aria-label="Spy School secret agent ID card with badge, photo, code name and fingerprint"></div>

    <h2 class="abs faq-title">FREQUENTLY ASKED QUESTIONS</h2>
    <div class="abs faq faq-l row-1"><h3>How many children can come to a Spy Birthday Party?</h3><p>We provide parties for groups of up to 40 children. For groups of up to 12 we will provide one entertainer, for larger groups we will provide more entertainers to ensure all the children get a great experience.</p></div>
    <div class="abs faq faq-r row-1"><h3>How old should the children be?</h3><p>The Spy Birthday party is aimed at children aged 6-12, but we can adapt it for younger ones too.</p></div>
    <div class="abs faq faq-l row-2"><h3>Where can we have a Spy Birthday Party?</h3><p>You can have a Spy Birthday Party anywhere, at your home, at a café or a church hall. If you need help finding a venue let us know and we can help find a suitable place.</p></div>
    <div class="abs faq faq-r row-2"><h3>How much does it cost?</h3><p>The cost depends on how many children will be taking part. For groups up to 12, with one entertainer running the party, it costs £175.00. For larger groups have a look at our Prices.</p></div>
    <div class="abs faq faq-l row-3"><h3>Who are our entertainers?</h3><p>All our entertainers are CRB checked and are fully trained to organise this type of birthday. After every party we ask our clients for feedback on the event, which helps our entertainers to continually evaluate and improve their performance.</p></div>
    <div class="abs faq faq-r row-3"><h3>Is this a great party?</h3><p>Many of our bookings come through recommendation. We have previous clients that would be happy to share their experience of a Spy Birthday Party; if you would like to talk to them let us know. You can also see some of our client feedback.</p><p>We'd like to help you organise a party your child will remember. We appreciate that people have busy lives and organising a party can be hard work – so let us make it easy for you!</p></div>
  </main>

  <footer>
    <div class="abs cta-bar"></div>
    <div class="abs cta-agent" role="img" aria-label="Young agent in a trilby hat"></div>
    <a class="abs btn btn-cta" href="#">INQUIRE NOW</a>
    <div class="abs cta-label">Or just give us a call:</div>
    <div class="abs cta-phone">020 3947 5018</div>
    <div class="abs footer-links"><a href="#">Contact us</a> | <a href="#">About us</a> | <a href="#">Terms and Conditions</a></div>
    <div class="abs copyright">Copyright © 2011-2013 Brightwater Events Ltd.</div>
  </footer>
</body>
</html>
```